metal roofing website

I have several domain names and a website that has been built. I need someone to recreate essentially the same website and change some photos and basic design to create the new sites. I have all of the files and c panel access to the lucky winner. If you can do a good job at a fair price I will have 100's of sites to send to you very soon. I have the site built and have all files just need it recreated on my server. the current site is www.dorvanemetalinc.com I am looking to get this done ASAP!!!

```html
<!DOCTYPE html>
<html lang="en">
<head>
<meta charset="UTF-8">
<title>Dorvane Metal Inc — Post Frame Buildings and Garages</title>
<link href="https://fonts.googleapis.com/css2?family=Poppins:wght@400;500;600&family=Lora:ital@1&family=Roboto:wght@400&display=swap" rel="stylesheet">
<style>
  :root {
    --topbar-bg: #f5f5f5;
    --topbar-text: #6b6b6b;
    --header-bg: #e4d3c3;
    --nav-text: #2b2320;
    --nav-active: #7a1a16;
    --brand-red: #b52a22;
    --brand-dark-red: #6e0f0e;
    --panel-bg: rgba(38, 36, 35, 0.86);
    --white: #ffffff;
  }
  * { margin: 0; padding: 0; box-sizing: border-box; }
  html, body { width: 1200px; height: 497px; overflow: hidden; background: var(--white); }
  .page { position: relative; width: 1200px; height: 497px; font-family: "Poppins", sans-serif; }

  .topbar { position: absolute; left: 0; top: 0; width: 1200px; height: 26px; background: var(--topbar-bg); }
  .topbar__tagline { position: absolute; left: 243px; top: 7px; font-family: "Roboto", sans-serif; font-size: 10px; color: var(--topbar-text); white-space: nowrap; }
  .topbar__links { position: absolute; right: 244px; top: 6px; display: flex; align-items: center; gap: 12px; font-family: "Roboto", sans-serif; font-size: 9.5px; color: var(--topbar-text); white-space: nowrap; }
  .topbar__social { display: flex; gap: 6px; margin-left: -6px; }
  .topbar__social span { width: 8px; height: 8px; border-radius: 50%; background: var(--topbar-text); display: block; }

  .header { position: absolute; left: 0; top: 26px; width: 1200px; height: 88px; background: var(--header-bg); }
  .brand { position: absolute; left: 236px; top: 30px; display: flex; align-items: center; gap: 7px; }
  .brand__mark { width: 22px; height: 22px; background: var(--brand-red); }
  .brand__name { font-size: 15px; font-weight: 600; color: var(--brand-red); line-height: 1; white-space: nowrap; }
  .nav { position: absolute; right: 244px; top: 37px; display: flex; align-items: center; font-size: 10.5px; color: var(--nav-text); white-space: nowrap; }
  .nav__item { display: flex; align-items: center; }
  .nav__item--active { color: var(--nav-active); }
  .nav__sep { margin: 0 11px; }
  .nav__caret { margin-left: 5px; }

  .hero { position: absolute; left: 0; top: 114px; width: 1200px; height: 319px; }
  .hero__photo { position: absolute; inset: 0; background: linear-gradient(100deg, #3f4a2c 0%, #5d6a46 22%, #b7b6a5 40%, #d9d7c6 62%, #c9cbc8 80%, #8d9a7a 100%); }
  .hero__panel { position: absolute; left: 242px; top: 124px; width: 268px; height: 152px; background: var(--panel-bg); color: var(--white); }
  .hero__kicker { position: absolute; left: 10px; top: 19px; font-size: 9.5px; font-weight: 500; letter-spacing: 0.1px; white-space: nowrap; }
  .hero__rule { position: absolute; left: 10px; top: 36px; width: 246px; height: 1px; background: rgba(255,255,255,0.55); }
  .hero__title { position: absolute; left: 10px; top: 49px; font-size: 19px; font-weight: 600; line-height: 23px; letter-spacing: 0.6px; white-space: nowrap; }
  .btn { position: absolute; display: flex; align-items: center; justify-content: center; font-size: 9.5px; font-weight: 500; color: var(--white); white-space: nowrap; }
  .btn--solid { left: 12px; top: 110px; width: 111px; height: 27px; background: var(--brand-red); }
  .btn--outline { left: 131px; top: 110px; width: 118px; height: 27px; border: 1px solid var(--brand-red); }

  .cta-band { position: absolute; left: 0; top: 433px; width: 1200px; height: 64px; background: var(--brand-red); }
  .cta-band__text { position: absolute; left: 243px; top: 20px; width: 560px; font-family: "Lora", serif; font-style: italic; font-size: 17.5px; line-height: 24px; color: var(--white); letter-spacing: 0; white-space: nowrap; }
  .cta-band__btn { position: absolute; left: 825px; top: 16px; width: 116px; height: 32px; background: var(--brand-dark-red); display: flex; align-items: center; justify-content: center; font-size: 9.5px; font-weight: 500; color: var(--white); white-space: nowrap; }
</style>
</head>
<body>
<div class="page">
  <div class="topbar">
    <p class="topbar__tagline">We Build Structures &amp; Relationships to Last</p>
    <div class="topbar__links">
      <span>Carrier</span>
      <span>Give Feedback</span>
      <span>Contact</span>
      <div class="topbar__social"><span></span><span></span><span></span><span></span><span></span></div>
    </div>
  </div>

  <header class="header">
    <div class="brand">
      <span class="brand__mark"></span>
      <span class="brand__name">Dorvane Metal Inc</span>
    </div>
    <nav class="nav">
      <span class="nav__item nav__item--active">Home</span><span class="nav__sep">-</span>
      <span class="nav__item">About Us</span><span class="nav__sep">-</span>
      <span class="nav__item">Services
        <svg class="nav__caret" width="7" height="5" viewBox="0 0 7 5"><path d="M0.5 0.8 L3.5 3.8 L6.5 0.8" fill="none" stroke="currentColor" stroke-width="1.1"/></svg>
      </span><span class="nav__sep">-</span>
      <span class="nav__item">Gallery</span><span class="nav__sep">-</span>
      <span class="nav__item">Contact Us</span>
    </nav>
  </header>

  <section class="hero">
    <div class="hero__photo" role="img" aria-label="Photo of a beige metal-sided post frame house with dormers, a cupola and a large garage door, framed by trees under a cloudy sky"></div>
    <div class="hero__panel">
      <p class="hero__kicker">WE ARE BRINGIG VISION TO LIFE</p>
      <div class="hero__rule"></div>
      <h1 class="hero__title">COMPLETE POST FRAME<br>AND GARAGES</h1>
      <a class="btn btn--solid">SEE MORE</a>
      <a class="btn btn--outline">GET A FREE QUOTE</a>
    </div>
  </section>

  <section class="cta-band">
    <p class="cta-band__text">Looking for a quality building component supplier for your project?</p>
    <a class="cta-band__btn">GET A FREE QUOTE</a>
  </section>
</div>
</body>
</html>
```